Angebotsflyer Velia Cosmetics
Zielgruppe
Kosmetikstudio, Einzelfirma Inhabergeführt
Klientel: Damen 30+ jährig
Naturkosmetik, keine apparative Kosmetik
Aufgabenstellung
Logo und Flyer (Eröffnung) im Anhang wurden bereits über Mustervogel.de gestaltet. Aus unserer Sicht schöne Vorlage.
Geforderter Leistungsumfang:
1. Flyer 3-seitig, DIN Lang (Hochformat). Angebotsflyer Velia Cosmetics. Idee gemäss Anhang, Aussenseiten schwarz, Innenseiten weiss (bessere Lesbarkeit). TEXT gemäss Anhang.
2. Flyer 1-seitig, DIN Lang (Hochformat). Kunden werben für Kunden. Dieser Flyer kann dem Angebotsflyer als Einlage mitgegeben werden und soll natürlich dem ähnlichen Stil des Angebotsflyers entsprechen. Ideen gemäss Anhang. Keine TEXT-Vorgabe im Anhang, kann durch Designer gestaltet werden. Als Prämie werden 15 CHF + 15 CHF auf die nächste Gesichtsbehandlung vergütet.

```html
<!DOCTYPE html>
<html lang="de">
<head>
<meta charset="utf-8">
<title>Velia Cosmetics – Angebotsflyer Innenseiten</title>
<link href="https://fonts.googleapis.com/css2?family=Montserrat:wght@400;500;600&display=swap" rel="stylesheet">
<style>
  :root{
    --stage:#e4e4e4;
    --paper:#fbfbfa;
    --paper-shade:#f4f3f1;
    --gold:#c39a5c;
    --gold-light:#e3cba0;
    --ink:#3b3b3b;
    --ink-soft:#5a5a5a;
    --photo-skin:#e8d6c8;
    --photo-glitter:#7c6b78;
    --photo-gift:#2a2a2a;
  }
  *{box-sizing:border-box;margin:0;padding:0}
  html,body{width:1200px;height:764px;overflow:hidden}
  body{background:var(--stage);font-family:"Montserrat",sans-serif;color:var(--ink)}
  .brochure{position:absolute;left:75px;top:11px;width:1050px;height:742px;display:flex;
    box-shadow:0 6px 24px rgba(0,0,0,.12);background:var(--paper)}
  .panel{position:relative;width:350px;height:100%;padding:0 30px}
  .panel + .panel{border-left:1px solid #ebe9e6}
  .panel--right{background:var(--paper-shade)}
  .header-photos{position:absolute;left:350px;top:0;width:700px;height:210px}
  .lead{font-size:10.5px;line-height:1.55;margin-top:60px}
  .brand-name{font-size:13px;font-weight:600;letter-spacing:.12em;color:var(--ink);margin:26px 0 10px;display:flex;align-items:center;gap:8px}
  .brand-name .dot{width:10px;height:10px;border-radius:50%;background:var(--gold)}
  .section-title{color:var(--gold);font-size:13px;font-weight:500;line-height:1.3;margin-bottom:6px}
  .copy{font-size:10.5px;line-height:1.55;color:var(--ink-soft)}
  .page-title{color:var(--gold);font-size:25px;font-weight:500;margin-top:222px}
  .intro{font-size:10.5px;margin:6px 0 20px}
  .service{display:flex;gap:14px;align-items:center;margin-bottom:10px}
  .service-photo{width:62px;height:62px;border-radius:50%;border:1.5px solid var(--gold);flex:none}
  .service .section-title{font-size:14px;margin:0}
  .checklist{list-style:none;font-size:10.5px;line-height:1.5;color:var(--ink-soft);margin:0 0 26px 4px}
  .checklist li{position:relative;padding-left:18px;margin-bottom:2px}
  .checklist li::before{content:"";position:absolute;left:0;top:4px;width:5px;height:9px;
    border:solid var(--gold);border-width:0 1.5px 1.5px 0;transform:rotate(45deg)}
  .panel--right .first{margin-top:232px}
  .gift{display:flex;gap:14px;align-items:flex-start;margin-top:6px}
  .gift-photo{width:80px;height:60px;flex:none;background:linear-gradient(180deg,#4a4a4a,var(--photo-gift))}
</style>
</head>
<body>
<div class="brochure">
  <section class="panel panel--left">
    <p class="lead">Mit viel Freude und Ueberzeugung sowie Wertschätzung auf unsere Natur arbeite ich mit spezialisierten Marken und ihren grossen Produktepaletten.</p>

    <div class="brand-name"><span class="dot"></span>AURELIA VEDA</div>
    <h3 class="section-title">Aurelia Veda – natürliche Kosmetikprodukte</h3>
    <p class="copy">Aurelia Veda Produkte sind überwiegend aus organischen Inhaltsstoffen formuliert und enthalten keine synthetische Duft- oder Farbstoffe. Die verwendeten ätherische Oele besitzen therapeutische Güte. Die ayurvedische Produktepalette von Aurelia Veda lässt für jeden Hauttyp und Bedürfnis das Richtige finden und trägt dazu bei, dass Körper, Geist und Seele im Einklang sind.</p>

    <div class="brand-name"><span class="dot"></span>HALDEN</div>
    <h3 class="section-title">Halden Cosmetics – ganz natürlich</h3>
    <p class="copy">Natürliche Inhaltsstoffe – höchste Qualität. Die hochwertigen Make-up Produkte der Halden Cosmetics lässt Sie strahlen. Sie sind biologisch, vegan, ohne Parabene und glutenfrei. Für jeden Teint findet sich die optimale Farbe und lässt Ihre Haut ebenmässig und natürlich aussehen. Ueberzeugen Sie sich selbst!</p>

    <div class="brand-name"><span class="dot"></span>SILKORA</div>
    <h3 class="section-title">Silkora – schonende, effektive Haarentfernung</h3>
    <p class="copy">Die natürliche Haarentfernung auch Body-Sugaring genannt, ist eine sanfte und langanhaltende Alternative zum Rasieren oder Wachsen. Silkora ist 100% natürlich, wasserlöslich und ohne Zusatz von Konservierungsstoffen. Ihre Haare wachsen feiner und langsamer nach – für ein rundum zartes Hautgefühl!</p>
  </section>

  <section class="panel panel--middle">
    <h2 class="page-title">Behandlungen</h2>
    <p class="intro">Folgende Behandlungen biete ich Ihnen gerne an:</p>

    <div class="service">
      <div class="service-photo" role="img" aria-label="Foto: Frau bei entspannender Gesichtsbehandlung" style="background:radial-gradient(circle,#f1e4da,#d9c2b1)"></div>
      <h3 class="section-title">Gesichtspflege<br>by Aurelia Veda</h3>
    </div>
    <ul class="checklist">
      <li>Wohlfühlgesichtsbehandlung – mit speziellem Fussritual</li>
      <li>Klassische Gesichtsbehandlung – perfekt auf Ihren Hauttyp abgestimmt</li>
      <li>Straffende Anti-Aging Gesichtsbehandlung</li>
      <li>Kurze Gesichtsbehandlung</li>
      <li>Gentleman's Corner – einfach entspannen!</li>
    </ul>

    <div class="service">
      <div class="service-photo" role="img" aria-label="Foto: Nahaufnahme eines geschminkten Auges mit Augenbraue" style="background:radial-gradient(circle,#c99a74,#9a6c4d)"></div>
      <h3 class="section-title">Wimpern- und<br>Augenbrauen färben</h3>
    </div>
    <p class="copy">Ein Muss für geheimnisvolle, elegant verführerische Blicke. Die dunkeln Wimpern sowie farblich abgestimmten Augenbrauen und Formen verleihen Ihrem Gesicht mehr Ausdruck. Wenig Aufwand – grosser Effekt.</p>
  </section>

  <section class="panel panel--right">
    <div class="service first">
      <div class="service-photo" role="img" aria-label="Foto: Make-up-Pinsel mit violettem Puder" style="background:radial-gradient(circle,#f2eef0,#b9a3bb)"></div>
      <h3 class="section-title">Make-up</h3>
    </div>
    <p class="copy">Natürlich, dezent, raffiniert oder gewagt? Für jeden Anlass das passende Make-up.</p>
    <ul class="checklist" style="margin-top:6px">
      <li>Tages Make-up</li>
      <li>Familenfest, Abend-/ oder Hochzeitsmake-up</li>
    </ul>

    <div class="service">
      <div class="service-photo" role="img" aria-label="Foto: glatte Frauenbeine nach der Haarentfernung" style="background:radial-gradient(circle,#f3e3d6,#d7a88a)"></div>
      <h3 class="section-title">Epilation<br>mit Silkora Sugaring</h3>
    </div>
    <p class="copy">Professionelle, natürlich schonende Haarentfernung.</p>
    <ul class="checklist" style="margin-top:6px">
      <li>Gesicht/Oberlippe/Kinn</li>
      <li>Körper/Beine/Achselhöhlen/Bikini</li>
      <li>In Kombinationen mit Preisvorteil</li>
    </ul>

    <h3 class="section-title" style="font-size:14px">Geschenkgutschein</h3>
    <div class="gift">
      <div class="gift-photo" role="img" aria-label="Foto: schwarze Geschenkbox mit goldener Schleife"></div>
      <p class="copy">Sie wollen eine besondere Freude machen? Ich habe eine Auswahl an liebevoll kreierten handgefertigten Geschenkkarten.</p>
    </div>
  </section>

  <svg class="header-photos" viewBox="0 0 700 210" aria-hidden="false">
    <defs>
      <linearGradient id="skin" x1="0" y1="0" x2="1" y2="1">
        <stop offset="0" stop-color="#f6efea"/><stop offset="1" stop-color="var(--photo-skin)"/>
      </linearGradient>
      <linearGradient id="glitter" x1="0" y1="0" x2="1" y2="1">
        <stop offset="0" stop-color="#8d7b88"/><stop offset="1" stop-color="#b6a6ad"/>
      </linearGradient>
      <linearGradient id="band" x1="0" y1="0" x2="1" y2="0">
        <stop offset="0" stop-color="var(--gold-light)"/><stop offset=".6" stop-color="var(--gold)"/><stop offset="1" stop-color="var(--gold-light)"/>
      </linearGradient>
    </defs>
    <polygon points="0,205 700,150 700,132 0,185" fill="url(#band)"/>
    <polygon role="img" aria-label="Foto: Kosmetikerin trägt Gesichtsmaske mit Pinsel auf" points="0,0 350,0 350,154 0,182" fill="url(#skin)"/>
    <polygon role="img" aria-label="Foto: violette Glitzerstruktur" points="350,0 700,0 700,128 350,154" fill="url(#glitter)"/>
  </svg>
</div>
</body>
</html>
```